Create Print and Packaging Designs for paint can

- Introduction

we need a design for a 15L (20kg) paint can, (label) the layout for this can is attached

- the paint brand name is VELKA , you find the logo attached, (VELKA means CUBE in Italian / spanish language)
- the product is a water based premium quality interior paint with full color range and many characteristics like : . Excellent adhesion ability works any surfaces. It does not crack, blister or spill. It is odorless, human and environment friendly. It has a great coverage capability and applied easily

- it is requested to make 2 cans design : VELKASOFT and VELKAMATT
design for both will be the same however color will change to differentiate
- language of the can label is french ... only velkamatt and velkasoft + 20 kg will be showed in both french and arabic as in the text attached
(IMPORTANT) This 2 paints are premium quality paint that is why design need to be luxurious and very attractive to people we request beauty and creativity and attention to details and especially clarity (CLEAN DESIGN)

- this is the can or the bucket on plane white in order to have an IDEA : [login to view URL]

- and this is some design examples from the bucket distributor website and please do not copy it is just to get more ideas

The text is attached for both VELKAMATT and VELKASOFT ... it is approximately the same ...

Once finish the work has to be given in the attached layout template (MOLD)
but during the contest you can show it as you want.

Material and texts :
please find the following :

1- text for both VELKAMATT and VELKASOFT
2- BRAND LOGO in ai and pdf ( VELKA is the brand)
3- layout of the can of 15 L
4- (current) design for both cans velkamatt and velkasoft

PS : it is better to put the icons which appears in the current design , we will provide the meaning of each in french soon ...

if any designer need any think please feel free to ask I'll support as match as I can
Best Of luck to all and let's make this contest great

```html
<!DOCTYPE html>
<html lang="fr">
<head>
<meta charset="utf-8">
<title>VELKASOFT – étiquette pot de peinture 20 kg</title>
<link rel="stylesheet" href="https://fonts.googleapis.com/css2?family=Open+Sans:ital,wght@0,400;0,700;1,600&family=Roboto+Condensed:wght@700&display=swap">
<style>
  :root {
    --stage: #cfcfcf;
    --paper: #ffffff;
    --mist: #eeeeee;
    --brand-red: #d8212f;
    --deep-red: #b51e2c;
    --wine: #9e1a27;
    --leaf: #2f7d3d;
    --leaf-dark: #1f5e2b;
    --ink: #2a2a2a;
    --soft-red: #ef8a90;
  }
  * { margin: 0; padding: 0; box-sizing: border-box; }
  html, body {
    width: 1200px;
    height: 831px;
    overflow: hidden;
    background: var(--stage);
  }
  .label {
    position: absolute;
    left: 120px;
    top: 115px;
    width: 960px;
    height: 600px;
    background: var(--paper);
    overflow: hidden;
  }
  .label-art {
    position: absolute;
    inset: 0;
    width: 960px;
    height: 600px;
  }
  .brand-block {
    position: absolute;
    left: 0;
    right: 0;
    top: 62px;
    display: flex;
    flex-direction: column;
    align-items: center;
  }
  .brand-name {
    font-family: "Open Sans", sans-serif;
    font-weight: 700;
    font-size: 58px;
    line-height: 1;
    letter-spacing: 2px;
    color: var(--brand-red);
  }
  .tagline {
    margin-top: 8px;
    font-family: "Open Sans", sans-serif;
    font-style: italic;
    font-weight: 600;
    font-size: 16px;
    line-height: 1.2;
    color: var(--ink);
  }
  .product-name {
    position: absolute;
    left: 0;
    right: 0;
    top: 165px;
    text-align: center;
    font-family: "Roboto Condensed", sans-serif;
    font-weight: 700;
    font-size: 60px;
    line-height: 1.1;
    letter-spacing: 2px;
    color: var(--ink);
  }
  .weight-badge {
    position: absolute;
    left: 424px;
    top: 324px;
    width: 112px;
    height: 112px;
    display: flex;
    align-items: center;
    justify-content: center;
    font-family: "Open Sans", sans-serif;
    font-weight: 700;
    font-size: 30px;
    color: var(--paper);
  }
  .volume-note {
    position: absolute;
    left: 572px;
    top: 354px;
    font-family: "Open Sans", sans-serif;
    font-size: 28px;
    line-height: 1;
    letter-spacing: 6px;
    color: var(--mist);
    opacity: 0.6;
  }
  .product-copy {
    position: absolute;
    left: 230px;
    top: 450px;
    width: 560px;
    font-family: "Open Sans", sans-serif;
    font-size: 15px;
    line-height: 22px;
    color: var(--soft-red);
  }
</style>
</head>
<body>
  <main class="label">
    <svg class="label-art" viewBox="0 0 960 600" aria-hidden="true">
      <path class="sheen" d="M480 0 C650 60 820 120 960 140 L960 0 Z" fill="var(--mist)"/>
      <path class="green-band-left" d="M0 300 C150 318 320 345 470 372 L440 395 C300 385 140 385 0 395 Z" fill="var(--leaf)"/>
      <path class="green-band-right" d="M960 255 L960 320 C870 325 770 332 700 338 C790 305 880 278 960 255 Z" fill="var(--leaf-dark)"/>
      <path class="red-field" d="M0 420 C250 400 480 398 700 372 C800 362 890 350 960 345 L960 600 L0 600 Z" fill="var(--brand-red)"/>
      <path class="red-field-shade" d="M0 520 C300 500 650 490 960 470 L960 600 L0 600 Z" fill="var(--deep-red)"/>
      <path class="red-field-base" d="M0 575 L960 575 L960 600 L0 600 Z" fill="var(--wine)"/>
      <circle class="badge-ring" cx="480" cy="380" r="56" fill="var(--brand-red)" stroke="var(--paper)" stroke-width="5"/>
    </svg>

    <header class="brand-block">
      <span class="brand-name">VELKA</span>
      <p class="tagline">Perfect solutions for building</p>
    </header>
    <h1 class="product-name">VELKASOFT</h1>

    <div class="weight-badge">20kg</div>
    <p class="volume-note">18 L</p>

    <p class="product-copy">Lorem ipsum dolor sit amet, consectetur adipiscing elit, sed do eiusmod tempor incididunt ut labore et dolore magna aliqua.</p>
  </main>
</body>
</html>
```